Company director needs a business card design

I am a semi-retired former senior finance executive who sits on a number of public and private company boards and do some consulting work. I work largely with emerging businesses but deal regularly with top end of town lawyers, bankers etc. I need a thoughtful but relatively conservative design which would also resonate with my younger client base. Some colour would be good. Information limited to name, address, office tel, mobile and email.

Industry/Entity Type

Finance

```html
<!DOCTYPE html>
<html lang="en">
<head>
<meta charset="utf-8">
<title>Business Card – Company Director</title>
<link href="https://fonts.googleapis.com/css2?family=Poppins:wght@600&family=Oswald:wght@600&family=Quicksand:wght@500&family=Questrial&display=swap" rel="stylesheet">
<style>
  :root {
    --page-bg: #ffffff;
    --card-edge: #95969a;
    --card-mid: #c4c5c8;
    --card-glow: #ececee;
    --ink: #0d0d0d;
    --divider: #0a0a0a;
  }
  html, body {
    margin: 0;
    padding: 0;
    width: 1200px;
    height: 1000px;
    overflow: hidden;
    background: var(--page-bg);
  }
  .canvas {
    position: relative;
    width: 1200px;
    height: 1000px;
  }
  .card {
    position: absolute;
    left: 43px;
    top: 183px;
    width: 861px;
    height: 515px;
    overflow: hidden;
    color: var(--ink);
  }
  .card-texture {
    position: absolute;
    inset: 0;
    background:
      radial-gradient(ellipse 55% 60% at 45% 48%, var(--card-glow) 0%, var(--card-mid) 55%, var(--card-edge) 100%);
  }
  .identity {
    position: absolute;
    left: 405px;
    top: 192px;
  }
  .name {
    margin: 0;
    font-family: "Poppins", sans-serif;
    font-weight: 600;
    font-size: 76px;
    line-height: 1;
    letter-spacing: -3px;
    white-space: nowrap;
  }
  .title {
    margin: 4px 0 0 2px;
    font-family: "Oswald", sans-serif;
    font-weight: 600;
    font-size: 44px;
    line-height: 1;
    letter-spacing: -0.5px;
  }
  .divider {
    position: absolute;
    left: 0;
    top: 329px;
    width: 100%;
    height: 19px;
    background: var(--divider);
  }
  .contact-line {
    position: absolute;
    display: flex;
    align-items: center;
    font-family: "Quicksand", sans-serif;
    font-weight: 500;
    font-size: 19px;
    letter-spacing: 0.3px;
    white-space: nowrap;
  }
  .contact-line svg { fill: var(--ink); flex: none; }
  .contact-address { left: 46px; top: 378px; }
  .contact-address svg { margin-right: 13px; }
  .contact-mobile { left: 50px; top: 425px; }
  .contact-mobile svg { margin-right: 20px; }
  .contact-office { left: 50px; top: 472px; }
  .contact-office svg { margin-right: 17px; }
  .contact-email {
    left: 270px;
    top: 472px;
    font-family: "Questrial", sans-serif;
    font-size: 22px;
    letter-spacing: 0;
  }
  .contact-email svg { margin-right: 18px; }
</style>
</head>
<body>
<main class="canvas">
  <section class="card">
    <div class="card-texture" role="img" aria-label="Soft silver-grey diamond lattice texture with a light glow in the centre"></div>

    <div class="identity">
      <h1 class="name">YOUR NAME</h1>
      <p class="title">TITLE</p>
    </div>

    <div class="divider"></div>

    <div class="contact-line contact-address">
      <svg width="25" height="23" viewBox="0 0 25 23" aria-hidden="true">
        <path d="M12.5 0 L25 11.5 L21.5 11.5 L21.5 23 L15 23 L15 15 L10 15 L10 23 L3.5 23 L3.5 11.5 L0 11.5 Z M18 2 H21 V6 L18 3.5 Z"/>
      </svg>
      <span>123 Abandoned Castle Highway Neverland</span>
    </div>

    <div class="contact-line contact-mobile">
      <svg width="14" height="25" viewBox="0 0 14 25" aria-hidden="true">
        <path d="M2.5 0 H11.5 A2.5 2.5 0 0 1 14 2.5 V22.5 A2.5 2.5 0 0 1 11.5 25 H2.5 A2.5 2.5 0 0 1 0 22.5 V2.5 A2.5 2.5 0 0 1 2.5 0 Z M2 3 V19 H12 V3 Z M7 20.5 A1.5 1.5 0 1 0 7 23.5 A1.5 1.5 0 1 0 7 20.5 Z" fill-rule="evenodd"/>
      </svg>
      <span>01234567890</span>
    </div>

    <div class="contact-line contact-office">
      <svg width="17" height="25" viewBox="0 0 17 25" aria-hidden="true">
        <path d="M4 0.5 L7 6.5 L5 8.5 C5 12 7 16 10 18.5 L12.5 16.8 L16.5 22 L13.5 24.8 C7 24 1 15 1 6 C1 3 2 1.5 4 0.5 Z"/>
      </svg>
      <span>222 333 444</span>
    </div>

    <div class="contact-line contact-email">
      <svg width="26" height="19" viewBox="0 0 26 19" aria-hidden="true">
        <path d="M0 0 H26 L13 10 Z M0 2.5 L8.5 9.5 L0 17 Z M26 2.5 V17 L17.5 9.5 Z M10 10.8 L13 13.2 L16 10.8 L26 19 H0 Z"/>
      </svg>
      <span>name@company.com</span>
    </div>
  </section>
</main>
</body>
</html>
```